Design logo, business cards, and web page for new web and bi development consulting company

I've started a Web and Business Intelligence development consulting company. We develop on Quorvantel's stack, Visual Sudio and SQL Server. We develop responsive web sites and business intelligence platforms. I plan on focusing on small to medium sized business as my client base. I need a logo, business cards, and a one page web site. We will do more with the web site with you in the next six months if the business survives. The name of the company is Belvorq Linkage Solutions, Belvorq for short.

Target Market(s)

small to medium sized businesses

Industry/Entity Type

Business

Contact Information for Business Card

logo
name
title
email
phone

Logo Text

Belvorq Linkage Solutions - web and data solutions

Coding

Coded - Design and coding required

Number of Pages Required

1 page

Font styles to use
Sans Serif

Colors
0355a3
0092cd
00a88f
6b449b

Requirements
Nice to have
• web and data solutions

```html
<!DOCTYPE html>
<html lang="en">
<head>
<meta charset="utf-8">
<title>Belvorq Linkage Solutions</title>
<link href="https://fonts.googleapis.com/css2?family=Lato:wght@300;400;700&family=Open+Sans:wght@400;600&display=swap" rel="stylesheet">
<style>
:root{
  --blue:#0355a3;
  --blue-bright:#0a6fd6;
  --ink:#333;
  --muted:#777;
  --soft:#999;
  --line:#e3e3e3;
  --band:#ebebeb;
  --footer:#4b4b4b;
  --footer-dark:#2c2c2c;
  --white:#fff;
}
*{margin:0;padding:0;box-sizing:border-box}
html,body{width:1200px;height:3593px;overflow:hidden}
body{position:relative;background:var(--white);font-family:'Open Sans',sans-serif;color:var(--ink)}

/* hero */
.hero{position:absolute;left:0;top:0;width:1200px;height:814px;overflow:hidden}
.hero-visual{position:absolute;inset:0;background:radial-gradient(circle at 330px 330px,#5aa8ff 0,#1d4f9c 14%,#0d2450 38%,#060d1e 72%,#03060f 100%)}
.logo{position:absolute;left:98px;top:28px;color:var(--white);font-family:'Lato',sans-serif;font-weight:400}
.logo-name{font-size:38px;line-height:44px}
.logo-sub{font-size:17px;line-height:22px}
.nav{position:absolute;top:48px;right:96px;display:flex;gap:30px;list-style:none}
.nav li{color:var(--white);font-size:13px;letter-spacing:.3px}
.hero-copy{position:absolute;right:98px;top:290px;width:520px;text-align:right;color:var(--white)}
.hero-title{font-family:'Lato',sans-serif;font-weight:400;font-size:48px;line-height:58px}
.hero-text{font-size:13px;line-height:17px;margin-top:12px;color:#dfe7f5}
.btn{position:absolute;display:flex;align-items:center;justify-content:center;font-size:15px;color:var(--white);border-radius:4px}
.btn-outline{left:752px;top:505px;width:168px;height:57px;border:2px solid var(--white)}
.btn-solid{left:934px;top:505px;width:168px;height:57px;background:var(--blue-bright)}
.slide-arrow{position:absolute;top:367px;width:26px;height:50px;background:var(--blue-bright);display:flex;align-items:center;justify-content:center}
.slide-arrow.prev{left:0}.slide-arrow.next{right:0}
.dots{position:absolute;top:746px;left:568px;display:flex;gap:6px}
.dots span{width:16px;height:16px;border-radius:50%;background:#8a8a8a}

/* services */
.section-title{position:absolute;left:0;width:1200px;text-align:center;font-family:'Lato',sans-serif;font-weight:300;color:#444}
.services-title{top:833px;font-size:36px}
.divider{position:absolute;left:505px;top:905px;width:190px;height:20px}
.services-sub{position:absolute;left:330px;top:960px;width:540px;text-align:center;font-size:15px;line-height:22px;color:var(--soft);font-family:'Lato',sans-serif}
.service{position:absolute;width:230px;text-align:center}
.service svg{display:block;margin:0 auto 10px}
.service h3{font-weight:400;font-size:16px;color:#555;margin-bottom:8px}
.service p{font-size:13px;line-height:17px;color:#777}

/* about */
.about{position:absolute;left:0;top:1550px;width:1200px;height:450px;background:var(--band);text-align:center}
.about-title{position:absolute;top:34px;width:100%;font-family:'Lato',sans-serif;font-weight:300;font-size:64px;color:#333}
.about-lead{position:absolute;top:136px;width:100%;font-family:'Lato',sans-serif;font-weight:400;font-size:50px;color:var(--blue)}
.about-sub{position:absolute;top:206px;width:100%;font-family:'Lato',sans-serif;font-weight:400;font-size:27px;color:#555}
.about-text{position:absolute;top:255px;left:180px;width:840px;font-size:13px;line-height:19px;color:var(--soft)}
.about-btn{left:500px;top:338px;width:200px;height:58px;background:var(--blue-bright)}

/* news & testimonials */
.col-head{position:absolute;font-size:17px;color:#333}
.col-rule{position:absolute;height:1px;background:var(--line)}
.col-rule::before{content:"";position:absolute;left:0;top:-1px;width:100px;height:3px;background:var(--blue-bright)}
.news-thumb{position:absolute;width:112px;height:112px}
.news-title{position:absolute;font-size:16px;color:var(--blue)}
.news-meta{position:absolute;font-size:10px;color:var(--soft)}
.news-text{position:absolute;width:332px;font-size:11px;line-height:15px;color:#888}
.quote-box{position:absolute;left:617px;top:2143px;width:484px;height:160px;border:1px solid var(--line)}
.quote-mark{position:absolute;left:23px;top:22px;width:30px;height:30px;background:var(--blue);color:#fff;font-family:'Lato',sans-serif;font-weight:700;font-size:28px;line-height:38px;text-align:center}
.quote-text{position:absolute;left:75px;top:32px;width:380px;font-size:12px;line-height:19px;color:#888}
.quote-tail{position:absolute;left:30px;bottom:-11px;width:20px;height:20px;background:#fff;border-right:1px solid var(--line);border-bottom:1px solid var(--line);transform:rotate(45deg)}
.pager{position:absolute;top:2064px;width:18px;height:18px;border:1px solid var(--line);font-size:10px;color:#bbb;text-align:center;line-height:16px}
.avatar{position:absolute;left:617px;top:2330px;width:52px;height:52px}
.author{position:absolute;left:692px;top:2343px;font-size:13px;color:#333}
.author-role{position:absolute;left:692px;top:2363px;font-size:11px;color:var(--blue)}

/* team */
.member{position:absolute;top:2510px;width:225px;height:330px;border:1px solid var(--line)}
.member-photo{width:223px;height:224px}
.member-name{margin:12px 0 0 14px;font-size:14px;color:#333}
.member-role{margin:4px 0 0 14px;font-size:11px;color:var(--blue)}
.member-social{display:flex;gap:10px;margin:20px 0 0 14px;padding-top:12px;border-top:1px solid #eee;width:196px}
.member-social span{width:10px;height:10px;border-radius:50%;background:#c8c8c8}

/* map */
.map{position:absolute;left:0;top:2898px;width:1200px;height:312px;background:linear-gradient(160deg,#dfe3d7 0%,#cfdcc3 35%,#c9d8e6 70%,#a9c6e6 100%)}

/* contact */
.contact{position:absolute;left:0;top:3222px;width:1200px;height:318px;background:var(--footer);color:var(--white)}
.contact-head{position:absolute;top:48px;display:flex;align-items:center;gap:8px;font-size:30px}
.contact-text{position:absolute;top:110px;font-size:14px;line-height:19px;color:#eee}
.socials{position:absolute;left:482px;top:226px;display:flex;gap:36px}
.socials span{width:26px;height:26px;border-radius:50%;background:#f2f2f2}
.bottom-bar{position:absolute;left:0;top:3540px;width:1200px;height:53px;background:var(--footer-dark);color:#ddd;font-size:12px}
.bottom-bar p{position:absolute;left:98px;top:18px}
</style>
</head>
<body>

<header class="hero">
  <div class="hero-visual" role="img" aria-label="Person holding a glowing globe surrounded by floating data screens in dark blue light"></div>
  <div class="logo">
    <div class="logo-name">Belvorq</div>
    <div class="logo-sub">Linkage Solutions</div>
  </div>
  <ul class="nav">
    <li>HOME</li><li>ABOUT</li><li>OUR TEAM</li><li>WORK</li><li>PRICING</li><li>SERVICES</li><li>BLOG</li><li>FEATURES</li><li>CONTACT</li>
  </ul>
  <div class="hero-copy">
    <h1 class="hero-title">TALENTED TEAM OF<br>DEVELOPERS</h1>
    <p class="hero-text">Lorem ipsum dolor sit amet conse ctetur adipisicing elit, sed do eiusmod tempor incididunt ut labore et dolore magna aliqua. Ut enim ad minim veniam, quis nostrud exercitation ullamco laboris nisi ut aliquip ex ea commodo consequat.</p>
  </div>
  <div class="btn btn-outline">LEARN MORE</div>
  <div class="btn btn-solid">DOWNLOAD</div>
  <div class="slide-arrow prev"><svg width="10" height="14" viewBox="0 0 10 14"><path d="M8 1 2 7l6 6" fill="none" stroke="#fff" stroke-width="2"/></svg></div>
  <div class="slide-arrow next"><svg width="10" height="14" viewBox="0 0 10 14"><path d="M2 1l6 6-6 6" fill="none" stroke="#fff" stroke-width="2"/></svg></div>
  <div class="dots"><span></span><span></span><span></span></div>
</header>

<section>
  <h2 class="section-title services-title">OUR SERVICES</h2>
  <svg class="divider" viewBox="0 0 190 20"><line x1="0" y1="10" x2="80" y2="10" stroke="#ddd"/><line x1="110" y1="10" x2="190" y2="10" stroke="#ddd"/><path d="M88 4l14 12M102 4 88 16" stroke="#0355a3" stroke-width="3"/></svg>
  <p class="services-sub">CHECK OUT SOME OF OUR MAIN CORE FEATURES CORVESSA IS A VERYPOWERFUL THEME PACKED WITH TONS OF SHORTCODES.</p>

  <div class="service" style="left:98px;top:1086px">
    <svg width="46" height="40" viewBox="0 0 46 40"><rect x="3" y="3" width="40" height="27" rx="2" fill="none" stroke="#222" stroke-width="4"/><rect x="14" y="34" width="18" height="4" fill="#222"/></svg>
    <h3>Web Development</h3><p>The path of a cosmonaut is not an easy, triumphant march to glory. You have to get to know the meaning not just of joy.</p>
  </div>
  <div class="service" style="left:357px;top:1086px">
    <svg width="46" height="40" viewBox="0 0 46 40"><path d="M3 34 15 18l8 8 19-20M3 24l10-12 8 6" fill="none" stroke="#222" stroke-width="3"/></svg>
    <h3>Analytics</h3><p>Dinosaurs are extinct today because they lacked opposable thumbs and the brainpower to build a space program.</p>
  </div>
  <div class="service" style="left:616px;top:1086px">
    <svg width="46" height="40" viewBox="0 0 46 40"><circle cx="23" cy="20" r="17" fill="#222"/><path d="M23 20V3a17 17 0 0 1 17 17z" fill="#fff"/><path d="M25 18V5a15 15 0 0 1 13 13z" fill="#222"/></svg>
    <h3>Database Structure</h3><p>The path of a cosmonaut is not an easy, triumphant march to glory. You have to get to know the meaning not just of joy.</p>
  </div>
  <div class="service" style="left:875px;top:1086px">
    <svg width="46" height="40" viewBox="0 0 46 40"><path d="M6 15h8l20-10v30L14 25H6z" fill="#222"/><rect x="12" y="25" width="6" height="10" fill="#222"/></svg>
    <h3>Advertising</h3><p>Dinosaurs are extinct today because they lacked opposable thumbs and the brainpower to build a space program.</p>
  </div>

  <div class="service" style="left:98px;top:1298px">
    <svg width="46" height="40" viewBox="0 0 46 40"><circle cx="19" cy="17" r="11" fill="none" stroke="#222" stroke-width="5"/><path d="M27 25l10 10" stroke="#222" stroke-width="6" stroke-linecap="round"/></svg>
    <h3>SEO</h3><p>Dinosaurs are extinct today because they lacked opposable thumbs and the brainpower to build a space program.</p>
  </div>
  <div class="service" style="left:357px;top:1298px">
    <svg width="46" height="40" viewBox="0 0 46 40"><path d="M40 4C18 4 8 14 10 32 28 32 38 22 40 4z" fill="#222"/><path d="M6 38 30 12" stroke="#fff" stroke-width="2"/></svg>
    <h3>Corporate Branding</h3><p>The path of a cosmonaut is not an easy, triumphant march to glory. You have to get to know the meaning not just of joy.</p>
  </div>
  <div class="service" style="left:616px;top:1298px">
    <svg width="46" height="40" viewBox="0 0 46 40"><path d="M38 3C28 4 20 10 15 20l6 6c10-5 16-13 17-23z" fill="#222"/><path d="M14 18l-7 1-4 6 9-1zM22 28l-1 7 6-4 1-9zM13 27l-6 9 9-6z" fill="#222"/></svg>
    <h3>Graphic Design</h3><p>Dinosaurs are extinct today because they lacked opposable thumbs and the brainpower to build a space program.</p>
  </div>
  <div class="service" style="left:875px;top:1298px">
    <svg width="46" height="40" viewBox="0 0 46 40"><rect x="13" y="1" width="20" height="38" rx="3" fill="none" stroke="#222" stroke-width="3"/><circle cx="23" cy="33" r="2" fill="#222"/></svg>
    <h3>Mobile Interface</h3><p>The path of a cosmonaut is not an easy, triumphant march to glory. You have to get to know the meaning not just of joy.</p>
  </div>
</section>

<section class="about">
  <h2 class="about-title">ABOUT</h2>
  <p class="about-lead">CREATING REALLY USER-FRIENDLY</p>
  <p class="about-sub">WEBSITES THAT WORK FOR YOUR BENEFIT</p>
  <p class="about-text">Lorem ipsum dolor sit amet conse ctetur adipisicing elit, sed do eiusmod tempor incididunt ut labore et dolore magna aliqua. Ut enim ad minim veniam, quis nostrud exercitation ullamco laboris nisi ut aliquip ex ea commodo consequat. Duis aute irure dolor in reprehenderit in voluptate velit esse cillum dolore eu fugiat nulla pariatur. Lorem ipsum dolor sit amet conse ctetur.</p>
  <div class="btn about-btn">READ MORE</div>
</section>

<section>
  <h3 class="col-head" style="left:98px;top:2060px">Latest News</h3>
  <div class="col-rule" style="left:98px;top:2098px;width:502px"></div>

  <div class="news-thumb" style="left:98px;top:2143px;background:linear-gradient(135deg,#1f3f86,#4d74b8)" role="img" aria-label="Blue newspaper headlines thumbnail"></div>
  <p class="news-title" style="left:237px;top:2148px">Little girl having her teeth checked</p>
  <p class="news-meta" style="left:237px;top:2174px">September 15, 2013 · Comments 4</p>
  <p class="news-text" style="left:237px;top:2195px">Cum sociis natoque penatibus et magnis dis parturient montes. Pro vel nibh et elit mollis commodo et nec augueque Mauris at justo eu lectus auctor porta vel ut libero.</p>

  <div class="news-thumb" style="left:98px;top:2278px;background:linear-gradient(135deg,#8b7a3a,#d6c98a)" role="img" aria-label="Newspaper headline word thumbnail"></div>
  <p class="news-title" style="left:237px;top:2280px">Close-up of medical equipment</p>
  <p class="news-meta" style="left:237px;top:2306px">September 15, 2013 · Comments 2</p>
  <p class="news-text" style="left:237px;top:2327px">Cum sociis natoque penatibus et magnis dis parturient montes. Pro vel nibh et elit mollis commodo et nec augueque Mauris at justo eu lectus auctor porta vel ut libero.</p>

  <h3 class="col-head" style="left:617px;top:2060px">Testimonials</h3>
  <div class="pager" style="left:1058px">‹</div><div class="pager" style="left:1080px">›</div>
  <div class="col-rule" style="left:617px;top:2098px;width:484px"></div>
  <div class="quote-box">
    <div class="quote-mark">“</div>
    <p class="quote-text">Cum sociis natoque penatibus et magnis dis parturient montes. Pro vel nibh et elit mollis commodo et nec augueque Mauris at justo eu lectus auctor porta vel ut libero. Susp mattis tellus vel augue mollis ultrices. Suspendisse poten.</p>
    <div class="quote-tail"></div>
  </div>
  <div class="avatar" style="background:linear-gradient(135deg,#6b6b6b,#c7c7c7)" role="img" aria-label="Client portrait"></div>
  <p class="author">Tobin Farrow</p>
  <p class="author-role">Patient of the clinic</p>
</section>

<section>
  <h3 class="col-head" style="left:98px;top:2436px">Our Team</h3>
  <div class="col-rule" style="left:98px;top:2473px;width:1003px"></div>

  <div class="member" style="left:98px">
    <div class="member-photo" style="background:linear-gradient(180deg,#d9d9d9,#b7a89a)" role="img" aria-label="Portrait of team member"></div>
    <p class="member-name">Corin Maddox</p><p class="member-role">Orthopedic Surgery</p>
    <div class="member-social"><span></span><span></span><span></span><span></span><span></span></div>
  </div>
  <div class="member" style="left:357px">
    <div class="member-photo" style="background:linear-gradient(180deg,#d4d4d4,#8f8c8a)" role="img" aria-label="Portrait of team member"></div>
    <p class="member-name">Teo Varnell</p><p class="member-role">Outpatient Surgery</p>
    <div class="member-social"><span></span><span></span><span></span><span></span><span></span></div>
  </div>
  <div class="member" style="left:617px">
    <div class="member-photo" style="background:linear-gradient(180deg,#d6d6d6,#7b5d4b)" role="img" aria-label="Portrait of team member"></div>
    <p class="member-name">Rhea Bramwell</p><p class="member-role">Laryngological Clinic</p>
    <div class="member-social"><span></span><span></span><span></span><span></span><span></span></div>
  </div>
  <div class="member" style="left:876px">
    <div class="member-photo" style="background:linear-gradient(180deg,#d8d8d8,#9a9a9a)" role="img" aria-label="Portrait of team member"></div>
    <p class="member-name">Sorin Halvet</p><p class="member-role">Gynecological Clinic</p>
    <div class="member-social"><span></span><span></span><span></span><span></span><span></span></div>
  </div>
</section>

<div class="map" role="img" aria-label="Street map of the office location"></div>

<footer class="contact">
  <div class="contact-head" style="left:110px">
    <svg width="24" height="24" viewBox="0 0 24 24"><path d="M5 2h4l2 6-3 2c1 3 3 5 6 6l2-3 6 2v4c0 2-2 3-4 3C9 21 3 15 3 5c0-2 1-3 2-3z" fill="#fff"/></svg>Call
  </div>
  <p class="contact-text" style="left:110px">+222 555 0147</p>

  <div class="contact-head" style="left:538px">
    <svg width="24" height="24" viewBox="0 0 24 24"><path d="M12 1a8 8 0 0 0-8 8c0 6 8 14 8 14s8-8 8-14a8 8 0 0 0-8-8z" fill="#fff"/><circle cx="12" cy="9" r="3" fill="#4b4b4b"/></svg>Visit
  </div>
  <p class="contact-text" style="left:500px;width:200px;text-align:center">P.O. Box 4418<br>902 W. Larkspur Rd.<br>Fenmore, IL 60417</p>

  <div class="contact-head" style="left:950px">
    <svg width="26" height="20" viewBox="0 0 26 20"><rect x="1" y="1" width="24" height="18" fill="#fff"/><path d="M1 1l12 10L25 1" fill="none" stroke="#4b4b4b" stroke-width="2"/></svg>Email
  </div>
  <p class="contact-text" style="left:925px">info@belvorqmail.com</p>

  <div class="socials"><span></span><span></span><span></span><span></span><span></span></div>
</footer>

<div class="bottom-bar"><p>Copyright © 2015 - All Rights Reserved</p></div>

</body>
</html>
```